Election features for a political website

The Hearthside Ledger (www.hearthsideledger.example)
Web banner designs
Please have a look at The Hearthside Ledger website (www.hearthsideledger.example). We are seeking to add an advertising style banner at the top of every page and post. It will run right across the page (1024 pixels) and be in the region of 200 pixels vertically. (Please advise on what looks best size wise.
The banner will be a slider, operated in a similar way to the current homepage slider. There will be four items on the slider, and so we need four designs that match the aesthetic feel of the website. Each slider will link through to posts on the website.
1.
Headline: OUR CANDIDATE OF THE DAY
Space for a name, head and shoulders picture of the person to be dropped in and a one line reason. This will need to be in an editable format as this image will be changed each day for one month.
2.
Headline: HERO OF THE DAY
Space for name and a one line reason. This will need to be in an editable format as this image will be changed each day for one month.
3.
Headline: VILLAIN OF THE DAY
Space for name of the person to be dropped in and a one line reason. This will need to be in an editable format as this image will be changed each day for one month.
4.
Headline: THL Poll – [Date]
If the election was today, who would you vote for?
Clickable options:
Brightfolders
Ashvel
Marden Alliancers
Vornu
Tally
Other
Can a poll widget be added to the banner? We would like this poll to reset each day and then pool the results into a graph day by day over a one month period.
Reason: Payment is now guaranteed. We would like to see more options.

```html
<!DOCTYPE html>
<html lang="en">
<head>
<meta charset="utf-8">
<title>Election feature banners</title>
<link href="https://fonts.googleapis.com/css2?family=Cinzel:wght@600;700&family=Tinos&display=swap" rel="stylesheet">
<style>
  :root {
    --ledger-blue: #0b4f8c;
    --ink: #1a1a1a;
    --body-grey: #444444;
    --link-navy: #0b3566;
    --panel-white: #ffffff;
    --panel-light: #f2f2f2;
    --stage: #000000;
    --photo-light: #e9e9e9;
    --photo-mid: #b9b9b9;
    --photo-dark: #7d7d7d;
  }
  * { margin: 0; padding: 0; box-sizing: border-box; }
  html, body { width: 1200px; height: 1000px; overflow: hidden; background: var(--stage); }
  .stage { position: relative; width: 1200px; height: 1000px; }

  .banner { position: absolute; left: 128px; width: 942px; height: 184px; overflow: hidden; }
  .banner--candidate { top: 47px; }
  .banner--hero { top: 283px; }
  .banner--villain { top: 516px; }
  .banner--poll { top: 755px; }

  .banner__shapes { position: absolute; inset: 0; }

  .banner__headline {
    position: absolute; left: 32px; top: 14px; height: 44px;
    display: flex; align-items: center; gap: 14px;
    font-family: "Cinzel", serif; font-weight: 700; color: #fff;
    font-size: 33px; letter-spacing: 0.5px; white-space: nowrap;
  }
  .banner--hero .banner__headline,
  .banner--villain .banner__headline { letter-spacing: 2.5px; font-size: 35px; top: 15px; }
  .headline__icon { width: 38px; height: 38px; fill: #fff; }

  .banner__reason {
    position: absolute; left: 34px; top: 86px; width: 540px;
    font-family: "Tinos", serif; font-size: 17px; line-height: 28px; color: var(--body-grey);
  }
  .banner__link {
    position: absolute; left: 32px; top: 148px;
    font-family: "Tinos", serif; font-size: 17px; color: var(--link-navy);
    text-decoration: underline; text-underline-offset: 3px;
  }
  .banner--hero .banner__link, .banner--villain .banner__link { font-size: 16px; top: 150px; }

  .banner__name {
    position: absolute; right: 22px; bottom: 7px;
    font-family: "Tinos", serif; font-size: 25px; color: #fff; white-space: nowrap;
  }

  .poll__title {
    position: absolute; left: 72px; top: 12px;
    font-family: "Cinzel", serif; font-weight: 700; font-size: 27px; color: #fff;
    letter-spacing: 0.5px; white-space: nowrap;
  }
  .poll__question {
    position: absolute; left: 26px; top: 66px;
    font-family: "Tinos", serif; font-size: 23px; color: var(--ink);
  }
  .poll__option {
    position: absolute; display: flex; align-items: center; gap: 8px;
    font-family: "Tinos", serif; font-size: 19px; color: var(--ink); white-space: nowrap;
  }
  .poll__radio {
    width: 12px; height: 12px; border: 1.5px solid #555; border-radius: 50%; background: #fff;
  }
  .poll__vote {
    position: absolute; left: 470px; top: 155px;
    font-family: "Tinos", serif; font-size: 18px; color: #fff;
  }
</style>
</head>
<body>
<main class="stage">

  <!-- Candidate of the day -->
  <section class="banner banner--candidate">
    <svg class="banner__shapes" width="942" height="184" viewBox="0 0 942 184">
      <defs>
        <linearGradient id="photoCandidate" x1="0" x2="1" y1="0" y2="1">
          <stop offset="0" stop-color="#f4f4f4"/><stop offset="0.6" stop-color="#dcdcdc"/><stop offset="1" stop-color="#f0f0f0"/>
        </linearGradient>
      </defs>
      <rect width="942" height="184" fill="var(--panel-white)"/>
      <polygon points="0,0 607,0 582,70 0,70" fill="var(--ledger-blue)"/>
      <polygon points="638,0 942,0 942,184 588,184" fill="url(#photoCandidate)" role="img" aria-label="Head and shoulders photo of the candidate"/>
      <polygon points="612,0 631,0 581,184 562,184" fill="var(--ledger-blue)"/>
      <polygon points="758,141 942,141 942,184 746,184" fill="var(--ledger-blue)"/>
    </svg>
    <h2 class="banner__headline">OUR CANDIDATE OF THE DAY</h2>
    <p class="banner__reason">Reason: Lorem ipsum dolor sit amet, consectetur adipiscing elit, sed do eiusmod tempor incididunt ut labore et dolore magna aliqua.</p>
    <a class="banner__link" href="#">Read Full Story Here</a>
    <span class="banner__name">Marian Holt</span>
  </section>

  <!-- Hero of the day -->
  <section class="banner banner--hero">
    <svg class="banner__shapes" width="942" height="184" viewBox="0 0 942 184">
      <defs>
        <linearGradient id="photoHero" x1="0" x2="1" y1="0" y2="0">
          <stop offset="0" stop-color="#cfcfcf"/><stop offset="0.35" stop-color="#8d8d8d"/><stop offset="1" stop-color="#e6e6e6"/>
        </linearGradient>
      </defs>
      <rect width="942" height="184" fill="var(--panel-light)"/>
      <polygon points="0,0 607,0 582,70 0,70" fill="var(--ledger-blue)"/>
      <polygon points="631,0 942,0 942,184 581,184" fill="url(#photoHero)" role="img" aria-label="Close-up portrait photo of the hero"/>
      <polygon points="608,0 624,0 576,184 560,184" fill="var(--ledger-blue)"/>
      <polygon points="758,141 942,141 942,184 746,184" fill="var(--ledger-blue)"/>
    </svg>
    <h2 class="banner__headline">
      <svg class="headline__icon" viewBox="0 0 24 24" aria-hidden="true"><path d="M2 10h4v12H2zM8 21V10l5-8c1.4 0 2.4 1.2 2 2.6L14 9h6.5c1.2 0 2 1.1 1.7 2.2l-2.3 8.3c-.3.9-1.1 1.5-2 1.5z"/></svg>
      HERO OF THE DAY
    </h2>
    <p class="banner__reason">Reason: Lorem ipsum dolor sit amet, consectetur adipiscing elit, sed do eiusmod tempor incididunt ut labore et dolore magna aliqua.</p>
    <a class="banner__link" href="#">Read Full Story Here</a>
    <span class="banner__name">Marian Holt</span>
  </section>

  <!-- Villain of the day -->
  <section class="banner banner--villain">
    <svg class="banner__shapes" width="942" height="184" viewBox="0 0 942 184">
      <defs>
        <linearGradient id="photoVillain" x1="0" x2="1" y1="0" y2="0">
          <stop offset="0" stop-color="#9a9a9a"/><stop offset="0.5" stop-color="#c9c9c9"/><stop offset="1" stop-color="#b0b0b0"/>
        </linearGradient>
      </defs>
      <rect width="942" height="184" fill="var(--panel-light)"/>
      <polygon points="0,0 607,0 582,70 0,70" fill="var(--ledger-blue)"/>
      <polygon points="631,0 942,0 942,184 581,184" fill="url(#photoVillain)" role="img" aria-label="Portrait photo of the villain in an office setting"/>
      <polygon points="608,0 624,0 576,184 560,184" fill="var(--ledger-blue)"/>
      <polygon points="758,141 942,141 942,184 746,184" fill="var(--ledger-blue)"/>
    </svg>
    <h2 class="banner__headline">
      <svg class="headline__icon" viewBox="0 0 24 24" aria-hidden="true"><path d="M2 2h4v12H2zM8 3v11l5 8c1.4 0 2.4-1.2 2-2.6L14 15h6.5c1.2 0 2-1.1 1.7-2.2L19.9 4.5C19.6 3.6 18.8 3 17.9 3z"/></svg>
      VILLAIN OF THE DAY
    </h2>
    <p class="banner__reason">Reason: Lorem ipsum dolor sit amet, consectetur adipiscing elit, sed do eiusmod tempor incididunt ut labore et dolore magna aliqua.</p>
    <a class="banner__link" href="#">Read Full Story Here</a>
    <span class="banner__name">Marian Holt</span>
  </section>

  <!-- Daily poll -->
  <section class="banner banner--poll">
    <svg class="banner__shapes" width="942" height="184" viewBox="0 0 942 184">
      <defs>
        <linearGradient id="photoPoll" x1="0" x2="1" y1="0" y2="1">
          <stop offset="0" stop-color="#b5b5b5"/><stop offset="0.5" stop-color="#d8d8d8"/><stop offset="1" stop-color="#8f8f8f"/>
        </linearGradient>
      </defs>
      <rect width="942" height="184" fill="var(--panel-light)"/>
      <polygon points="0,0 606,0 590,56 0,56" fill="var(--ledger-blue)"/>
      <polygon points="630,0 942,0 942,184 581,184" fill="url(#photoPoll)" role="img" aria-label="Pile of campaign vote badges"/>
      <polygon points="610,0 625,0 576,184 561,184" fill="var(--ledger-blue)"/>
      <polygon points="458,150 564,150 555,182 452,182" fill="var(--ledger-blue)"/>
    </svg>
    <h2 class="poll__title">THL POLL –&nbsp; MAR 17 2015</h2>
    <p class="poll__question">If the election was today, who would you vote for?</p>
    <label class="poll__option" style="left:25px;top:109px"><span class="poll__radio"></span>Brightfolders</label>
    <label class="poll__option" style="left:209px;top:109px"><span class="poll__radio"></span>Ashvel</label>
    <label class="poll__option" style="left:343px;top:109px"><span class="poll__radio"></span>Marden Alliancers</label>
    <label class="poll__option" style="left:25px;top:144px"><span class="poll__radio"></span>Vornu</label>
    <label class="poll__option" style="left:209px;top:144px"><span class="poll__radio"></span>Tally</label>
    <label class="poll__option" style="left:343px;top:144px"><span class="poll__radio"></span>Other</label>
    <a class="poll__vote" href="#">Vote Now</a>
  </section>

</main>
</body>
</html>
```